Velmora Systems 4-Brochure Package

Design an overall look-n-feel (a template). Then implement for a family of 4 brochures:
1. Unified Communications
2. App & Mobile Development
3. Telemedicine
4. Managed Services

Will need to incorporate content, diagrams, and photographs into each of the brochures (all provided).

Photographs need to be "layered" and colorized to match the overall brand concept of intersecting circles where the middle is the "velmora" (and the Q resides). See Concepts provided. (Colors: Pantone Blue 072C, Pantone 279C- 80% Opacity, Process Cyan 80% Opacity)

Utilize image "Velmora Infrastructure Background" as the background (refer to look of website listed below).

New website is under development and can be viewed at: http://brindlestudio-example.com/velmora/

Target Market(s)

Chief Information Officers and IT Professionals, Industries include health, hospitals, technology, manufacturing, government.

Industry/Entity Type

Communications

Requirements
Must have
• Need to use the blue-colorized photos (raw images provided). Need to match branded color palette (noted above in brief) - Refer to Brand Comps provided also.

Include both addresses:

SACRAMENTO:
1730 Kestrel Ridge Way, Suite 410
Sacramento, CA 95840
916.555.0142
Toll-free: 1.866.555.0197

CHICO:
468 Larkspur Lane, Suite 220
Chico, CA 95931
530.555.0168
Toll-free: 1.866.555.0197

```html
<!DOCTYPE html>
<html lang="en">
<head>
<meta charset="utf-8">
<title>Velmora Systems – Managed Services</title>
<link rel="stylesheet" href="https://fonts.googleapis.com/css2?family=Questrial&display=swap">
<style>
  :root {
    --brand-blue: #2a3f99;
    --brand-blue-deep: #1b2f7e;
    --photo-dark: #15275f;
    --photo-mid: #2f5cae;
    --photo-light: #7fb2e6;
    --accent-cyan: #2bb5e6;
    --paper: #ffffff;
    --logo-blue: #27409a;
    --page-bg: #e9ecf2;
  }
  html, body {
    margin: 0;
    padding: 0;
    overflow: hidden;
    background: var(--page-bg);
  }
  .brochure-cover {
    position: relative;
    width: 788px;
    height: 1200px;
    background: var(--paper);
    overflow: hidden;
    font-family: "Questrial", "Century Gothic", sans-serif;
  }
  .title-band {
    position: absolute;
    left: 0;
    top: 0;
    width: 100%;
    height: 300px;
    background: linear-gradient(180deg, var(--brand-blue) 0%, var(--brand-blue-deep) 100%);
  }
  .cover-title {
    position: absolute;
    right: 34px;
    top: 204px;
    margin: 0;
    color: var(--paper);
    font-weight: 400;
    font-size: 46px;
    letter-spacing: 0.5px;
  }
  .title-rule {
    position: absolute;
    left: 360px;
    right: 0;
    top: 266px;
    height: 3px;
    background: var(--paper);
  }
  .hero-photo {
    position: absolute;
    left: 0;
    top: 300px;
    width: 100%;
    height: 412px;
    background:
      radial-gradient(ellipse at 40% 35%, rgba(160, 200, 240, 0.55) 0%, rgba(160, 200, 240, 0) 45%),
      linear-gradient(90deg, var(--photo-light) 0%, var(--photo-mid) 35%, var(--photo-dark) 75%, var(--photo-mid) 100%);
  }
  .accent-rule {
    position: absolute;
    left: 0;
    top: 718px;
    width: 100%;
    height: 10px;
    background: var(--accent-cyan);
  }
  .feature-circle {
    position: absolute;
    left: 30px;
    top: 540px;
    width: 270px;
    height: 270px;
    border-radius: 50%;
    border: 10px solid var(--paper);
    box-sizing: border-box;
    background: radial-gradient(circle at 45% 40%, var(--photo-light) 0%, var(--photo-mid) 45%, var(--photo-dark) 100%);
  }
  .brand-signature {
    position: absolute;
    left: 416px;
    top: 1042px;
    display: flex;
    align-items: center;
    gap: 18px;
    color: var(--logo-blue);
  }
  .brand-dot {
    width: 66px;
    height: 66px;
    border-radius: 50%;
    background: var(--logo-blue);
  }
  .brand-name {
    font-size: 34px;
    letter-spacing: 1px;
    line-height: 1;
  }
</style>
</head>
<body>
  <main class="brochure-cover">
    <section class="title-band">
      <h1 class="cover-title">Managed Services</h1>
      <div class="title-rule"></div>
    </section>

    <div class="hero-photo" role="img" aria-label="Blue-tinted photo of an IT technician working at a terminal in a server room"></div>
    <div class="accent-rule"></div>

    <div class="feature-circle" role="img" aria-label="Circular blue-tinted photo of server racks"></div>

    <div class="brand-signature">
      <span class="brand-dot"></span>
      <span class="brand-name">Velmora Systems</span>
    </div>
  </main>
</body>
</html>
```